Premium Olive Oil Bottle Label

Need a double bottle label for our premium olive oil (front and back). Please refer to the brief attached. The label needs to incorporate the elements from the logo designs that we provide in attachment into a single design language. The front panel should capture attention and the back panel provide a story of our unique product.

Target Market(s)

US and Europe

Industry/Entity Type

Food Production

Font styles to use
Other font styles liked:
• Please refer to the Brief

Colors

Designer to choose colors to be used in the design.

Requirements
Must have
• Integrate the elements in the brief into a single premium execution.
Nice to have
• Feel free to use the provided visual elements as a base for your further creative exploration.
Should not have
• Too many colors. Please propose a restricted color palette as the bottle is black matte. The design needs to deliver premium appeal and be distinctive.

```html
<!DOCTYPE html>
<html lang="en">
<head>
<meta charset="utf-8">
<title>Le Beau Champ – Olive Oil Labels</title>
<link rel="stylesheet" href="https://fonts.googleapis.com/css2?family=Josefin+Sans:wght@400;600;700&display=swap">
<style>
  :root {
    --backdrop: #b5bba8;
    --label-black: #1c1c1c;
    --label-black-soft: #262626;
    --gold: #c9a85a;
    --gold-light: #e8d39a;
    --gold-dark: #9a7a35;
    --ink-light: #efefef;
  }
  * { margin: 0; padding: 0; box-sizing: border-box; }
  html, body { width: 1180px; height: 1200px; overflow: hidden; }
  body {
    background: var(--backdrop);
    font-family: "Josefin Sans", sans-serif;
    position: relative;
  }

  /* ---------- front label ---------- */
  .front-label {
    position: absolute;
    left: 140px; top: 268px;
    width: 456px; height: 680px;
  }
  .front-label svg.front-shape { position: absolute; inset: 0; }
  .front-emblem {
    position: absolute; left: 0; right: 0; top: 38px;
    display: flex; flex-direction: column; align-items: center; gap: 4px;
  }
  .front-emblem .mark-dot {
    width: 46px; height: 46px; border-radius: 50%;
    background: var(--gold);
  }
  .front-emblem .mark-name {
    font-size: 9px; font-weight: 700; letter-spacing: 1.5px; color: var(--gold);
  }
  .front-title {
    position: absolute; left: 0; right: 0; top: 234px;
    text-align: center; color: var(--gold);
    font-weight: 700; font-size: 66px; line-height: 61px; letter-spacing: 3px;
    text-transform: uppercase;
  }
  .front-subtitle {
    position: absolute; left: 0; right: 0; top: 426px;
    text-align: center; color: var(--gold);
    font-weight: 700; font-size: 16px; letter-spacing: 0.6px;
  }
  .front-appellation {
    position: absolute; left: 0; right: 0; top: 448px;
    text-align: center; color: var(--ink-light);
    font-size: 15px; letter-spacing: 1px; font-variant: small-caps;
  }
  .front-badge {
    position: absolute; left: 131px; top: 480px;
    width: 194px; height: 112px;
    text-align: center;
  }
  .front-badge svg { position: absolute; inset: 0; }
  .front-badge .badge-title {
    position: relative; margin-top: 16px;
    color: var(--gold); font-size: 19px; letter-spacing: 1px; font-variant: small-caps;
  }
  .front-badge .badge-lines {
    position: relative; margin-top: 8px;
    color: var(--ink-light); font-size: 12px; line-height: 14.5px;
    font-variant: small-caps; letter-spacing: 0.3px;
  }

  /* ---------- back label ---------- */
  .back-label {
    position: absolute;
    left: 698px; top: 126px;
    width: 329px; height: 965px;
    border-radius: 66px;
    background: linear-gradient(160deg, var(--gold-light), var(--gold) 35%, var(--gold-dark) 70%, var(--gold-light));
    padding: 6px;
  }
  .back-inner {
    position: relative; width: 100%; height: 100%;
    border-radius: 60px;
    background: linear-gradient(180deg, var(--label-black-soft), var(--label-black));
  }
  .back-brand {
    position: absolute; left: 0; right: 0; top: 48px;
    display: flex; flex-direction: column; align-items: center; gap: 14px;
  }
  .back-brand .mark-dot {
    width: 46px; height: 46px; border-radius: 50%; background: var(--gold);
  }
  .back-brand .brand-name {
    color: var(--gold); font-weight: 700; font-size: 26px; letter-spacing: 1.5px;
  }
  .rule {
    position: absolute; left: 50px; right: 50px; height: 1px; background: var(--gold);
  }
  .rule.top { top: 174px; }
  .rule.bottom { top: 726px; }
  .story {
    position: absolute; left: 50px; right: 50px; top: 202px;
    display: flex; flex-direction: column;
  }
  .story-heading {
    color: var(--gold); font-weight: 700; font-size: 14px; letter-spacing: 0.2px;
    white-space: nowrap; text-align: center;
    margin-bottom: 10px;
  }
  .story-text,
  .reservations {
    color: var(--ink-light); font-weight: 600; font-size: 10.4px; line-height: 19.6px;
    letter-spacing: 0.1px;
    text-transform: uppercase; text-align: justify; text-align-last: left;
  }
  .reservations { margin-top: 20px; }
  .origin {
    position: absolute; left: 0; right: 0; top: 752px;
    text-align: center; color: var(--gold); font-size: 13px; letter-spacing: 0.8px;
  }
  .producer-address {
    position: absolute; left: 0; right: 0; top: 779px;
    text-align: center; color: var(--gold); font-size: 15px; line-height: 16px;
    font-variant: small-caps; letter-spacing: 0.8px;
  }
  .bottle-number {
    position: absolute; left: 0; right: 0; top: 838px;
    display: flex; justify-content: center; align-items: center; gap: 6px;
    color: var(--gold); font-size: 14px; font-variant: small-caps; letter-spacing: 0.8px;
  }
  .bottle-number .number-field {
    width: 84px; height: 20px;
    background: linear-gradient(90deg, var(--gold-dark), var(--gold), var(--gold-light), var(--gold));
  }
  .best-before {
    position: absolute; left: 0; right: 0; top: 886px;
    text-align: center; color: var(--ink-light); font-size: 15px;
    font-variant: small-caps; letter-spacing: 0.5px;
  }
  .volume {
    position: absolute; left: 0; right: 0; top: 908px;
    text-align: center; color: var(--gold); font-size: 14px;
    font-variant: small-caps; letter-spacing: 1px;
  }
</style>
</head>
<body>

<section class="front-label" aria-label="Front label">
  <svg class="front-shape" width="456" height="680" viewBox="0 0 456 680">
    <defs>
      <linearGradient id="goldRim" x1="0" y1="0" x2="1" y2="1">
        <stop offset="0" stop-color="#e8d39a"/>
        <stop offset="0.45" stop-color="#c9a85a"/>
        <stop offset="1" stop-color="#f0dfa8"/>
      </linearGradient>
      <radialGradient id="patternTone" cx="0.5" cy="0.55" r="0.5">
        <stop offset="0.55" stop-color="#1c1c1c"/>
        <stop offset="0.8" stop-color="#3c3c3c"/>
        <stop offset="1" stop-color="#4a4a4a"/>
      </radialGradient>
    </defs>
    <ellipse cx="228" cy="340" rx="228" ry="340" fill="url(#goldRim)"/>
    <ellipse cx="228" cy="340" rx="220" ry="332" fill="#1c1c1c"/>
    <ellipse cx="228" cy="340" rx="214" ry="326" fill="url(#patternTone)"
             role="img" aria-label="Hand-drawn line pattern of olive branches, leaves, swirls, a bottle and a bowl of olives"/>
  </svg>

  <div class="front-emblem">
    <span class="mark-dot"></span>
    <span class="mark-name">LE BEAU CHAMP</span>
  </div>

  <h1 class="front-title">Le<br>Beau<br>Champ</h1>
  <p class="front-subtitle">HUILE D'OLIVE VIERGE EXTRA</p>
  <p class="front-appellation">AOC Haute-Provence</p>

  <div class="front-badge">
    <svg width="194" height="112" viewBox="0 0 194 112">
      <rect x="2" y="2" width="190" height="108" rx="50" fill="#1c1c1c" stroke="#c9a85a" stroke-width="2.5"/>
      <line x1="44" y1="43" x2="150" y2="43" stroke="#c9a85a" stroke-width="1"/>
    </svg>
    <div class="badge-title">Organic</div>
    <div class="badge-lines">
      Limited production<br>
      Late harvest Hand-picked<br>
      Single cold-press<br>
      Unfiltered
    </div>
  </div>
</section>

<section class="back-label" aria-label="Back label">
  <div class="back-inner">
    <header class="back-brand">
      <span class="mark-dot"></span>
      <span class="brand-name">LE BEAU CHAMP</span>
    </header>
    <div class="rule top"></div>

    <article class="story">
      <h2 class="story-heading">THE STORY OF THIS BOTTLE</h2>
      <p class="story-text">
        Nested in the hills of Provence, Le Beau Champ is a wild and magical place where forest opens up to vineyards and olive groves. We fell in love with it, and you would too! It's in these hills that Aglandau olives were grown since Roman times, and we were happy to bring them back. Our production is entirely organic, we pick our olives by hand and only at the point of maturity. We don't harvest our Aglandaus until very late in the autumn, and use a single mechanical cold-press extraction. The reward? A very special extra virgin oil with its full-on bold taste, hints of artichokes and fresh-cut grass, and remarkably low acidity.
      </p>
      <p class="reservations">Reservations for 2019 harvest open at info@lebeauchamp.com</p>
    </article>

    <div class="rule bottom"></div>
    <p class="origin">MADE IN FRANCE</p>
    <p class="producer-address">SCEA Le Beau Champ<br>Chemin des Oliviers<br>Valserène 04990</p>
    <div class="bottle-number"><span>Bottle No:</span><span class="number-field"></span></div>
    <p class="best-before">Best enjoyed before 08/2020</p>
    <p class="volume">Vol. 500ml</p>
  </div>
</section>

</body>
</html>
```